New Business Card Design Project

2 sided business card required. I have attached some previous designs of items we have had made so you can see the logo etc. we Want the card to look professional and modern. for the final design upload for winning designer please note I need to be able to edit the names / phone numbers on the card design as I need to get them made for different staff.
Updates

extending time so designers can have time to submit

Target Market(s)

new customers

Industry/Entity Type

transport / earthmoving

Contact Information for Business Card

name, phone number email address

Requirements
Nice to have
• professional / impressive looking card (first impressions to customers count)
Should not have
• do not put our mobile number on the design use a generic number

```html
<!DOCTYPE html>
<html lang="en">
<head>
<meta charset="utf-8">
<title>KTR Pty Ltd – Business Card</title>
<link href="https://fonts.googleapis.com/css2?family=Nunito+Sans:ital,wght@0,300;0,400;0,600;0,800;1,800&display=swap" rel="stylesheet">
<style>
  :root {
    --stage: #161616;
    --card-dark: #0b0b0b;
    --mesh: #1c1c1e;
    --dirt: #b8693c;
    --dirt-deep: #6e3f25;
    --chrome: #c9cacc;
    --paper: #f2f2f3;
    --ink: #3a3a3a;
    --ink-soft: #555;
    --white: #ffffff;
    --band: #0d0d0d;
  }
  * { box-sizing: border-box; margin: 0; padding: 0; }
  html, body {
    width: 1171px; height: 1200px; overflow: hidden;
    background: var(--stage);
    font-family: "Nunito Sans", Arial, sans-serif;
  }
  .card {
    position: absolute; left: 201px;
    width: 769px; height: 441px;
    border-radius: 17px; overflow: hidden;
    background: var(--card-dark);
    box-shadow: 0 0 40px rgba(255,255,255,0.12);
  }
  .card--front { top: 140px; }
  .card--back { top: 620px; }

  .card__backdrop {
    position: absolute; inset: 0;
    background:
      linear-gradient(180deg,
        var(--card-dark) 0%,
        var(--mesh) 30%,
        #242424 45%,
        #3b2d24 60%,
        var(--dirt-deep) 72%,
        var(--dirt) 88%,
        #c27a4a 100%);
  }

  .brand {
    position: absolute; left: 0; right: 0; top: 52px;
    text-align: center;
    color: var(--chrome);
    font-weight: 800;
    line-height: 1;
  }
  .brand__name { font-size: 118px; letter-spacing: 6px; }
  .brand__suffix {
    position: absolute; left: 619px; top: 102px;
    font-size: 26px;
  }

  .nameplate {
    position: absolute; left: 444px; top: 243px;
    width: 303px; height: 52px;
    background: var(--white);
    color: var(--ink);
    font-size: 34px; line-height: 52px;
    padding-left: 30px;
    font-weight: 300;
  }
  .nameplate strong { font-weight: 600; }

  .brush {
    position: absolute; background: var(--paper);
  }
  .brush--contact {
    left: 0; top: 334px; width: 325px; height: 102px;
    clip-path: polygon(0 6%, 20% 2%, 45% 8%, 70% 0, 96% 5%, 92% 30%, 100% 55%, 94% 78%, 98% 96%, 70% 100%, 40% 93%, 15% 100%, 0 96%);
  }
  .brush--address {
    left: 411px; top: 327px; width: 352px; height: 102px;
    clip-path: polygon(3% 8%, 30% 0, 60% 6%, 88% 1%, 100% 10%, 97% 40%, 100% 70%, 95% 92%, 65% 100%, 35% 94%, 8% 100%, 0 75%, 5% 45%, 0 20%);
  }

  .contact {
    position: absolute; left: 40px; top: 352px;
    list-style: none; color: var(--ink);
    font-size: 15px; line-height: 23px;
  }
  .contact li { display: flex; align-items: center; gap: 14px; }
  .contact svg { width: 13px; height: 13px; fill: var(--ink); }

  .address {
    position: absolute; left: 507px; top: 352px;
    color: var(--ink-soft); font-size: 17px; line-height: 25px;
  }

  .services-band {
    position: absolute; left: 0; top: 204px; width: 713px; height: 80px;
    background: var(--band);
    clip-path: polygon(0 0, 92% 4%, 100% 20%, 96% 50%, 100% 80%, 90% 100%, 0 100%);
  }
  .services-title {
    position: absolute; left: 48px; top: 212px;
    color: var(--white);
    font-size: 48px; font-weight: 800; font-style: italic;
    letter-spacing: 1px;
  }
  .brush--services {
    left: 4px; top: 288px; width: 760px; height: 138px;
    clip-path: polygon(0 10%, 10% 2%, 35% 6%, 60% 0, 85% 5%, 100% 2%, 97% 35%, 100% 62%, 96% 90%, 75% 98%, 50% 92%, 25% 100%, 3% 94%, 6% 60%, 0 35%);
  }
  .services {
    position: absolute; top: 300px;
    list-style: none; color: var(--ink);
    font-size: 15px; line-height: 26px;
  }
  .services--left { left: 102px; }
  .services--right { left: 473px; }
  .services li { display: flex; align-items: center; gap: 12px; }
  .services li::before {
    content: ""; width: 17px; height: 15px;
    background: #2a2a2a; border-radius: 2px;
  }
</style>
</head>
<body>

<section class="card card--front">
  <div class="card__backdrop" role="img" aria-label="Dark metal mesh texture above a photo of road-train trucks on red outback dirt"></div>
  <div class="brand"><span class="brand__name">KTR</span></div>
  <div class="brand brand__suffix">Pty Ltd</div>

  <div class="nameplate"><strong>Mark</strong> Delaney</div>

  <div class="brush brush--contact"></div>
  <ul class="contact">
    <li><svg viewBox="0 0 24 24"><path d="M6.6 10.8a15 15 0 0 0 6.6 6.6l2.2-2.2c.3-.3.7-.4 1-.2 1.1.4 2.3.6 3.6.6.6 0 1 .4 1 1V20c0 .6-.4 1-1 1A17 17 0 0 1 3 4c0-.6.4-1 1-1h3.5c.6 0 1 .4 1 1 0 1.3.2 2.5.6 3.6.1.3 0 .7-.2 1z"/></svg>+ 61 400 123 456</li>
    <li><svg viewBox="0 0 24 24"><path d="M2 5h20v14H2z M2 5l10 8 10-8" /></svg>mark@ktrhaulage.com.au</li>
    <li><svg viewBox="0 0 24 24"><circle cx="12" cy="12" r="10"/></svg>www.ktrhaulage.com.au</li>
  </ul>

  <div class="brush brush--address"></div>
  <p class="address">your address,home no<br>road no 123,gpo code<br>country</p>
</section>

<section class="card card--back">
  <div class="card__backdrop" role="img" aria-label="Dark metal mesh texture above a photo of trucks on red outback dirt"></div>
  <div class="brand"><span class="brand__name">KTR</span></div>
  <div class="brand brand__suffix">Pty Ltd</div>

  <div class="services-band"></div>
  <h2 class="services-title">OUR SERVICE</h2>

  <div class="brush brush--services"></div>
  <ul class="services services--left">
    <li>What is Lorem Ipsum?</li>
    <li>What is Lorem Ipsum?</li>
    <li>What is Lorem Ipsum?</li>
    <li>What is Lorem Ipsum?</li>
  </ul>
  <ul class="services services--right">
    <li>What is Lorem Ipsum?</li>
    <li>What is Lorem Ipsum?</li>
    <li>What is Lorem Ipsum?</li>
    <li>What is Lorem Ipsum?</li>
  </ul>
</section>

</body>
</html>
```